Larkmoor Health- Core Values Graphic for Visual Appeal

I would like a poster that could take these written core values from our organization and create a graphic that we could use for our staff and employees. I would also like to incorporate our branding into this project. Thank you!

Target Market(s)

To helps patients and employees understand the core values of our organization

Industry/Entity Type

Healthcare

Requirements
Must have
• Match our branding
Nice to have
• Please use your creativity!
Should not have
• Overly complex/ busy

```html
<!DOCTYPE html>
<html lang="en">
<head>
<meta charset="UTF-8">
<title>Larkmoor Health — Our Core Values</title>
<link href="https://fonts.googleapis.com/css2?family=Poppins:wght@700&family=Montserrat:wght@400;500;800&family=Ubuntu:wght@400&display=swap" rel="stylesheet">
<style>
  :root {
    --sky: #56bfdd;
    --sky-light: #8fd6ec;
    --heading-blue: #1a6fae;
    --white: #ffffff;
    --outline: rgba(255, 255, 255, 0.45);
    --dot: #1f4f73;
    --brand-ink: #3b3b3b;
    --brand-dot: #1ea0dc;
  }
  * { margin: 0; padding: 0; box-sizing: border-box; }
  html, body { width: 900px; height: 1200px; overflow: hidden; }
  body { background: var(--sky); }
  .poster {
    position: relative; width: 900px; height: 1200px; overflow: hidden;
    background: var(--sky); color: var(--white);
  }
  .title {
    position: absolute; left: 42px; top: 78px; width: 405px;
    font-family: "Poppins", sans-serif; font-weight: 700;
    font-size: 86px; line-height: 76px; letter-spacing: -1px; text-align: right;
  }
  .intro {
    position: absolute; left: 479px; top: 140px; width: 320px;
    font-family: "Ubuntu", sans-serif; font-size: 17.5px; line-height: 20.2px;
  }
  .puzzle { position: absolute; left: 0; top: 0; }
  .value-heading {
    position: absolute; font-family: "Montserrat", sans-serif; font-weight: 800;
    font-size: 31px; letter-spacing: 1px; color: var(--heading-blue);
  }
  .value-text {
    position: absolute; font-family: "Montserrat", sans-serif; font-weight: 400;
    font-size: 12.4px; line-height: 15px; letter-spacing: 0.2px;
  }
  .dots { position: absolute; border-top: 2px dotted var(--dot); }
  .dots-vertical { position: absolute; border-left: 2px dotted var(--dot); }
  .photo { position: absolute; border: 1px solid rgba(0,0,0,0.15); }
  .treatment-photo {
    position: absolute; left: 330px; top: 880px; width: 570px; height: 320px;
    background: radial-gradient(ellipse at 70% 80%, #e6eef2 0%, #b9d9e6 35%, rgba(86,191,221,0) 75%);
  }
  .brand {
    position: absolute; left: 720px; top: 1098px;
    display: flex; align-items: center; gap: 8px;
  }
  .brand-dot { width: 14px; height: 14px; border-radius: 50%; background: var(--brand-dot); }
  .brand-name {
    font-family: "Montserrat", sans-serif; font-weight: 800; font-size: 19px;
    color: var(--brand-ink);
  }
</style>
</head>
<body>
<main class="poster">
  <h1 class="title">Our Core Values</h1>
  <p class="intro">These core values are the spirit of who we are as a healthcare team. They guide our actions, unite us in purpose, and ensure that we provide world-class care while fostering a positive and supportive atmosphere within our team</p>

  <svg class="puzzle" width="900" height="1200" viewBox="0 0 900 1200" aria-hidden="true">
    <g fill="none" stroke="var(--outline)" stroke-width="3">
      <path d="M471.7 361.5 A265 265 0 0 1 707.5 597.3 L637.9 604.6 A195 195 0 0 0 464.4 431.1 Z"/>
      <path d="M707.5 652.7 A265 265 0 0 1 471.7 888.5 L464.4 818.9 A195 195 0 0 0 637.9 645.4 Z"/>
      <path d="M416.3 888.5 A265 265 0 0 1 180.5 652.7 L250.1 645.4 A195 195 0 0 0 423.6 818.9 Z"/>
      <path d="M180.5 597.3 A265 265 0 0 1 416.3 361.5 L423.6 431.1 A195 195 0 0 0 250.1 604.6 Z"/>
    </g>
  </svg>

  <div class="photo" role="img" aria-label="Team group photo in the clinic" style="left:241px;top:389px;width:185px;height:101px;background:linear-gradient(135deg,#6c6f74,#2c2e33);"></div>
  <div class="photo" role="img" aria-label="Practitioner treating a patient" style="left:326px;top:490px;width:100px;height:150px;background:linear-gradient(160deg,#3d4a3f,#1c1f22);"></div>
  <div class="photo" role="img" aria-label="Treatment room with patient on table" style="left:426px;top:470px;width:154px;height:102px;background:linear-gradient(135deg,#d9d4cc,#8a8079);"></div>
  <div class="photo" role="img" aria-label="Front desk consultation" style="left:426px;top:572px;width:124px;height:92px;background:linear-gradient(135deg,#5a5650,#2a2624);"></div>
  <div class="photo" role="img" aria-label="Practitioner explaining care to a patient" style="left:331px;top:640px;width:96px;height:146px;background:linear-gradient(150deg,#c9c4bd,#3a3c40);"></div>
  <div class="photo" role="img" aria-label="Reviewing an X-ray with a patient" style="left:429px;top:664px;width:125px;height:86px;background:linear-gradient(135deg,#7a5a4f,#c7c0b8);"></div>

  <h2 class="value-heading" style="left:119px;top:338px;">FAMILY</h2>
  <div class="dots" style="left:118px;top:378px;width:153px;"></div>
  <div class="dots-vertical" style="left:269px;top:378px;height:8px;"></div>
  <p class="value-text" style="left:33px;top:388px;width:200px;">At the heart of our mission is the commitment to provide high-quality, affordable healthcare in a comforting and uplifting family-oriented environment. Just as our community is our extended family, every patient is a cherished member of our healthcare family. We treat each individual with the same care, compassion, and respect we would offer to our own loved ones.</p>

  <h2 class="value-heading" style="left:609px;top:322px;">EXCELLENCE</h2>
  <div class="dots" style="left:608px;top:373px;width:66px;"></div>
  <p class="value-text" style="left:684px;top:385px;width:180px;">In line with our goal, we aspire not only to alleviate pain but also to inspire patients to become active participants in their well-being. We believe in empowering our patients through education and compassion. Our pursuit of excellence is unwavering, driven by our dedication to continuously improve our services at every level, ensuring that our community receives nothing less than exceptional care.</p>

  <h2 class="value-heading" style="left:46px;top:704px;">INTEGRITY</h2>
  <div class="dots" style="left:139px;top:746px;width:101px;"></div>
  <p class="value-text" style="left:48px;top:762px;width:208px;">In our healthcare team, 'Integrity' is non-negotiable. Our purpose is deeply rooted in ethics, integrity, and professional standards. We operate with the utmost integrity in every aspect of our work, adhering to the highest ethical principles. We understand that trust is the foundation of healthcare, and we are committed to maintaining the trust our community places in us.</p>

  <h2 class="value-heading" style="left:636px;top:667px;">SERVICE</h2>
  <div class="dots" style="left:634px;top:716px;width:30px;"></div>
  <div class="dots-vertical" style="left:662px;top:716px;height:68px;"></div>
  <p class="value-text" style="left:670px;top:723px;width:205px;">Our vision is grounded in the belief that every person possesses the innate potential for true health. We aim to facilitate the body's natural healing response by providing the highest level of service. Our hope for each patient extends beyond healing; we aspire to help you fulfill your life's mission and purpose abundantly, supporting you in your journey to well-being.</p>

  <div class="treatment-photo" role="img" aria-label="Patient lying down receiving a gentle neck adjustment"></div>

  <div class="brand">
    <span class="brand-dot"></span>
    <span class="brand-name">Larkmoor Health</span>
  </div>
</main>
</body>
</html>
```